Homepage for the brisk-trail Web Application

At the end of this text, you will find a link to a website that is under construction for a webApp that I intend to launch soon. The contest goal is for you to make redesign the homepage in a nice, fresh, modern Style. Only design, no coding necessary. It needs to have a responsive version for small screens like smart phones. Attached is the text for it, and some images that you may use. You are welcome to find or create additional supporting images. You can use PixVaultimages.com or similar service to find new images as long as I can purchase the non-exclusive use rights for the images at similar prices. The contest is just for the home page. However, the winner, if I like the work and we can agree on a fair price, could be contracted on a one-on-one basis to do the rest of the site. You are welcome to suggest minor changes like font sizes and minor variations on the Header banner, but that banner is consistent with the user interface of the application therefore should not change too much. The information should flow somewhat continually without much use of side bars or things like that.
https://www.brisk-trail-example.com
Sincerely,
Marco R. Delgado

```html
<!DOCTYPE html>
<html lang="en">
<head>
<meta charset="utf-8">
<title>Brisk-Trail — Home</title>
<link href="https://fonts.googleapis.com/css2?family=Roboto:wght@400;500;700&display=swap" rel="stylesheet">
<style>
:root{
  --blue:#2e78bd;
  --navy:#0c2b5c;
  --orange:#ff7e56;
  --mint:#eef4f2;
  --ink:#1f2a33;
  --white:#ffffff;
}
*{box-sizing:border-box;margin:0;padding:0}
html,body{width:1200px;height:4664px;overflow:hidden;background:var(--white)}
body{position:relative;font-family:'Roboto',Arial,sans-serif;color:var(--ink)}
.page{position:absolute;left:72px;top:0;width:1056px;height:4664px;background:var(--mint)}
.abs{position:absolute}
.site-header{left:0;top:0;width:1056px;height:139px;background:var(--blue)}
.brand{left:38px;top:36px;display:flex;align-items:center;gap:14px;color:var(--white);font-size:50px;font-weight:400}
.brand-dot{width:62px;height:62px;border-radius:50%;background:var(--white)}
.menu-icon{right:44px;top:48px}
.hero{left:0;top:139px;width:1056px;height:607px;background:linear-gradient(120deg,#e9e4da 0%,#cfc6b6 45%,#8d8576 100%)}
.hero-title{left:60px;top:138px;width:500px;text-align:center;color:var(--navy);font-size:49px;font-weight:500;letter-spacing:4px;line-height:56px}
.menu-note{left:640px;top:30px;width:360px;text-align:center;font-size:37px;font-weight:700;letter-spacing:3px;line-height:40px;color:#000}
.btn{position:absolute;display:flex;align-items:center;justify-content:center;background:var(--orange);color:var(--navy);border-radius:40px;font-weight:500;font-size:35px;letter-spacing:4px}
.btn-about{left:182px;top:393px;width:261px;height:67px}
.btn-shadow{box-shadow:0 18px 26px rgba(0,0,0,.22)}
.art{border-radius:50%;background:linear-gradient(135deg,#8fd0d6 0%,#ff7e56 60%)}
.section-title{left:60px;width:936px;text-align:center;color:var(--navy);font-size:46px;font-weight:500;letter-spacing:3px;line-height:55px}
.body-text{left:55px;width:950px;font-size:28.5px;letter-spacing:3px;line-height:37.6px;color:var(--ink)}
.sub-title{font-weight:700;font-size:28px;letter-spacing:3px;margin-bottom:9px}
.divider{left:420px;width:217px;height:8px;background:var(--navy)}
.bullets{list-style:none}
.bullets li{margin-bottom:10px}
.site-footer{left:0;top:4540px;width:1056px;height:124px;background:var(--blue);color:var(--white);font-size:17px;font-weight:700;letter-spacing:2px}
.site-footer span{position:absolute;top:52px}
</style>
</head>
<body>
<div class="page">
  <header class="abs site-header">
    <div class="abs brand"><span class="brand-dot"></span>brisk-trail</div>
    <svg class="abs menu-icon" width="46" height="42" viewBox="0 0 46 42"><g stroke="#fff" stroke-width="6" stroke-linecap="round"><line x1="3" y1="4" x2="43" y2="4"/><line x1="3" y1="21" x2="43" y2="21"/><line x1="3" y1="38" x2="43" y2="38"/></g></svg>
    <svg class="abs" style="left:780px;top:70px" width="200" height="110" viewBox="0 0 200 110"><path d="M40 105 C40 40 100 10 175 8" fill="none" stroke="#000" stroke-width="6"/></svg>
  </header>
  <section class="abs hero" role="img" aria-label="Photo of hands flipping through folders in a filing drawer">
    <div class="abs menu-note">menu and login will be in here</div>
    <h1 class="abs hero-title">Find that document or item instantly.</h1>
    <span class="btn btn-about">about us</span>
  </section>

  <div class="abs art" style="left:420px;top:868px;width:202px;height:217px" role="img" aria-label="Illustration of a person climbing out of a phone screen holding a key"></div>
  <h2 class="abs section-title" style="top:1132px">Keeping track of all your paper documents and other belongings has never been easier.</h2>
  <p class="abs body-text" style="top:1344px">Brisk-trail is a system that allows you to quickly search for the location of every item that you store or file. It is an essential tool for keeping track of paper documents. In addition, it is incredibly valuable for storing any other kind of physical items. Giving you the ability to quickly find any item, even years after it has been stored. More importantly, using Brisk-trail along with some best practice techniques, could allow you to save considerable space without losing fast accessibility of your items.</p>
  <div class="abs divider" style="top:1882px"></div>

  <div class="abs art" style="left:420px;top:2033px;width:202px;height:208px" role="img" aria-label="Illustration of a person seated on a phone screen sorting files"></div>
  <h2 class="abs section-title" style="top:2290px">Why use a storage management system like Brisk-Trail?</h2>
  <div class="abs body-text" style="top:2462px">
    <p class="sub-title">Managing paper documents</p>
    <p>It is quite common for most people and businesses to receive a variety of such documents that need to be filed. The problem is how to efficiently do it in a way that any of it can easily be found, even in a distant future. We normally put them in folders on file drawers sorted by some criteria. But which criterion is the right standard for all kinds of documents? There is no right criterion for every kind of document.</p>
  </div>
  <span class="btn btn-shadow" style="left:394px;top:2924px;width:260px;height:69px">read more</span>
  <div class="abs divider" style="top:3151px"></div>

  <div class="abs art" style="left:420px;top:3297px;width:202px;height:208px" role="img" aria-label="Illustration of a person on a phone screen carrying a document box"></div>
  <h2 class="abs section-title" style="top:3578px">Why Brisk-Trail?</h2>
  <ul class="abs body-text bullets" style="top:3648px">
    <li>• It is extremely easy to use.</li>
    <li>• It is Versatile. Since each catalog can have 1 or many levels of depth &nbsp;&nbsp;(folders and sub-folders). Brisk-trail does not force you to use a specific filing or storage methodology.</li>
    <li>• It is really affordable. Checkout our pricing plans.</li>
    <li>• Since it is online, your data is available almost anywhere in the world.</li>
    <li>• Your data always travels encrypted.</li>
  </ul>
  <span class="btn btn-shadow" style="left:327px;top:4162px;width:405px;height:81px">check our pricing</span>
  <span class="btn btn-shadow" style="left:327px;top:4289px;width:405px;height:81px">start 30 days trial</span>

  <footer class="abs site-footer">
    <span style="left:22px">-- contact --</span>
    <span style="left:335px">Copyright © 2016 Northgate Works LLC</span>
    <span style="right:40px">-- social media --</span>
  </footer>
</div>
</body>
</html>
```